THE NAME OF THE COMPANY IS: VERDANT HOLLOWS. Services including: Excavation , Custom Property Designs, Sustainable Vegetable Gardens, Beautiful Floriculture. Licensed Contractor with 35 years experience. I am looking for 4 simple Icons: One a tractor, signifying the Excavation work, one a pencil and paper or ruler or something to signify Custom Designs, one a vegetable and one a flower. Similar Icons to the Moss Harbor Logos (attached). The Icons will all be simple but easily identifiable. All of them should look in the same style. I am thinking about a color screen of various olive toned greens. See PMS color chart attached.Probably a white reverse in green tone squares. I'd be interested in different layouts of a business card which will translate to signs and truck door magnets for a full sized truck. It'd also need it to translate to stationary and give away items.

Target Market(s)

The target market is a homeowner with disposable inclome to afford a high end Landscape Artist.

Industry/Entity Type

Business

Contact Information for Business Card

Verdant Hollows
Excavation, Custom Designs, Sustainable Gardens, Floriculture
Howard Pellin
Contractor
Ca. Lic. # C27-591046
PO Box 208716 Carlsbad, Ca 92013
760-382-9174

Colors
acd036
33b7a4

Requirements
Must have
• The company name VERDANT HOLLOWS needs to be prominent with the tag line: Excavation, Custom Property Designs, Sustainable Gardens and Floraculture being centered underneath the name. Be creative with the card color and use different shades of the greens I provided for the icons.

```html
<!DOCTYPE html>
<html lang="en">
<head>
<meta charset="utf-8">
<title>Verdant Hollows — Business Card</title>
<link rel="stylesheet" href="https://fonts.googleapis.com/css2?family=Dosis:wght@300;500&family=Oswald:wght@500&display=swap">
<style>
  :root {
    --backdrop: #e6e4e1;
    --card: #f7f8f7;
    --olive: #7f8c52;
    --olive-dark: #6f7c45;
    --blush: #dccfcf;
  }
  * { margin: 0; padding: 0; box-sizing: border-box; }
  html, body {
    width: 1200px;
    height: 900px;
    overflow: hidden;
    background: var(--backdrop);
  }
  .stage {
    width: 1200px;
    height: 900px;
    display: flex;
    align-items: center;
    justify-content: center;
  }
  .business-card {
    width: 840px;
    height: 480px;
    background: var(--card);
    box-shadow: 0 6px 24px rgba(0,0,0,0.12);
    display: flex;
    flex-direction: column;
    align-items: center;
    padding-top: 44px;
    color: var(--olive);
  }
  .brand {
    display: flex;
    flex-direction: column;
    align-items: center;
  }
  .brand-mark {
    width: 170px;
    height: 170px;
    background: var(--blush);
  }
  .brand-name {
    margin-top: 14px;
    font-family: "Dosis", sans-serif;
    font-weight: 300;
    font-size: 64px;
    letter-spacing: 4px;
    line-height: 1;
    color: var(--olive);
    white-space: nowrap;
  }
  .tagline {
    margin-top: 8px;
    font-family: "Dosis", sans-serif;
    font-weight: 500;
    font-size: 15px;
    letter-spacing: 1px;
    text-transform: uppercase;
    color: var(--olive);
    white-space: nowrap;
  }
  .contact {
    margin-top: 36px;
    display: flex;
    flex-direction: column;
    align-items: center;
    gap: 14px;
    font-family: "Oswald", sans-serif;
    font-weight: 500;
    font-size: 16px;
    letter-spacing: 0.6px;
    text-transform: uppercase;
    color: var(--olive-dark);
  }
  .contact-line {
    display: flex;
    align-items: center;
    gap: 10px;
    white-space: nowrap;
  }
  .contact-icon {
    width: 24px;
    height: 24px;
    flex: none;
  }
</style>
</head>
<body>
<main class="stage">
  <article class="business-card">
    <div class="brand">
      <span class="brand-mark"></span>
      <h1 class="brand-name">VERDANT HOLLOWS</h1>
    </div>
    <p class="tagline">Excavation • Custom Property Designs • Sustainable Gardens • Floraculture</p>
    <div class="contact">
      <p class="contact-line">
        <svg class="contact-icon" viewBox="0 0 24 24" aria-hidden="true">
          <circle cx="12" cy="12" r="12" fill="var(--olive)"/>
          <path d="M6 12 L12 6.5 L18 12 M8 11 V17.5 H16 V11" fill="none" stroke="#fff" stroke-width="1.6" stroke-linejoin="round"/>
        </svg>
        Howard Pellin Contractor Ca. Lic. # C27-591046 PO Box 208716 Carlsbad, Ca 92013
      </p>
      <p class="contact-line">
        <svg class="contact-icon" viewBox="0 0 24 24" aria-hidden="true">
          <circle cx="12" cy="12" r="12" fill="var(--olive)"/>
          <rect x="8.5" y="5.5" width="7" height="13" rx="1.3" fill="none" stroke="#fff" stroke-width="1.5"/>
          <circle cx="12" cy="16" r="0.9" fill="#fff"/>
        </svg>
        760-382-9174
      </p>
    </div>
  </article>
</main>
</body>
</html>
```